'Bright Ledger Hidden Keys' Book Cover

I need a professional book cover design for my new upcoming book that shows people how to get a high credit score.

Here are my two websites:

https://www.moneywordbank-lexa.info
https://moneywordbank-lexa.com/

I am looking for a clean, professional design that pops (emotional touch) and separates from the other books that are on the market. Cover aspect ratio 1:4 for Pagewisp version and 1:5 for the paperback version. Yellow or blue are good colors - but not must. See the basic examples that I provided. File delivery format PDF.

Book Title: Bright Ledger Hidden Keys
Byline: The Quick Lift And Mend Manual for Stellar Borrowing

Currently on Brindlecart pre-order:
https://www.brindlecart.example/Bright-Ledger-Hidden-Keys-Stellar-ebook/dp/Q48MPLRT71

I am the author of 36 published books on Brindlecart. My author profile is here:
brindlecart.example/author/gideonvarly

Targeted audience: People that want to improve or repair their bad credit score.

Target Market(s)

People/consumers in the US that want to improve or repair their credit score.

Industry/Entity Type

Consumer

Font styles to use
Sans Serif

Colors

Designer to choose colors to be used in the design.

Requirements
Must have
• Author name, Title, byline, and graphic element(s).
Nice to have
• - 2020 edition logo / batch

```html
<!DOCTYPE html>
<html lang="en">
<head>
<meta charset="utf-8">
<title>Bright Ledger Hidden Keys — Cover Options</title>
<link rel="stylesheet" href="https://fonts.googleapis.com/css2?family=Bebas+Neue&family=Open+Sans:wght@300;600;700;800&display=swap">
<style>
  :root {
    --paper: #ffffff;
    --cover-yellow: #f8cc12;
    --ink: #1c2a2e;
    --card-blue: #38a9e0;
    --card-blue-soft: #7cc6ec;
    --title-white: #ffffff;
    --label-grey: #9a9a9a;
  }
  * { margin: 0; padding: 0; box-sizing: border-box; }
  html, body {
    width: 1068px;
    height: 1200px;
    overflow: hidden;
    background: var(--paper);
  }
  .board {
    position: relative;
    width: 1068px;
    height: 1200px;
  }
  .cover {
    position: absolute;
    top: 200px;
    width: 439px;
    height: 658px;
    background: var(--cover-yellow);
    overflow: hidden;
  }
  .cover--three { left: 82px; }
  .cover--four { left: 561px; top: 199px; }

  .series {
    position: absolute;
    top: 256px;
    left: 0;
    width: 100%;
    display: flex;
    justify-content: center;
    align-items: center;
    gap: 7px;
    font-family: "Open Sans", sans-serif;
    font-weight: 700;
    font-size: 11px;
    letter-spacing: 3.3px;
    color: var(--ink);
  }
  .cover .series { top: 57px; }
  .series__square { width: 11px; height: 8px; background: var(--ink); }
  .series__bar { width: 34px; height: 8px; background: var(--ink); }

  .title {
    position: absolute;
    top: 80px;
    left: 36px;
    width: 368px;
    height: 124px;
  }
  .title text {
    font-family: "Bebas Neue", sans-serif;
    fill: var(--title-white);
  }

  .hero-art {
    position: absolute;
    left: 122px;
    top: 251px;
    width: 214px;
    height: 199px;
    border-radius: 8px;
    background: linear-gradient(180deg, #f6f3e6 0%, var(--card-blue) 55%, #2f97cb 100%);
  }

  .rule {
    position: absolute;
    left: 154px;
    top: 496px;
    width: 130px;
    height: 2px;
    background: var(--ink);
  }
  .subtitle {
    position: absolute;
    top: 508px;
    left: 0;
    width: 100%;
    text-align: center;
    font-family: "Open Sans", sans-serif;
    color: var(--ink);
    font-size: 20px;
    line-height: 23px;
  }
  .subtitle__light { display: block; font-weight: 300; }
  .subtitle__bold { display: block; font-weight: 800; letter-spacing: 0.4px; }

  .author {
    position: absolute;
    top: 584px;
    left: 0;
    width: 100%;
    text-align: center;
    font-family: "Open Sans", sans-serif;
    font-weight: 600;
    font-size: 19px;
    letter-spacing: 1px;
    color: var(--ink);
  }

  .corner-card {
    position: absolute;
    left: 357px;
    top: 517px;
    width: 82px;
    height: 141px;
  }

  .option-label {
    position: absolute;
    top: 894px;
    width: 200px;
    text-align: center;
    font-family: "Open Sans", sans-serif;
    font-weight: 600;
    font-size: 12px;
    letter-spacing: 3px;
    color: var(--label-grey);
  }
  .option-label--three { left: 191px; }
  .option-label--four { left: 676px; }
</style>
</head>
<body>
<main class="board">

  <section class="cover cover--three">
    <p class="series"><span class="series__square"></span>VARLY FINANCIAL LITERACY PROGRAM<span class="series__bar"></span></p>
    <svg class="title" viewBox="0 0 368 124" aria-label="Bright Ledger Hidden Keys">
      <text x="0" y="56" font-size="78" textLength="368" lengthAdjust="spacingAndGlyphs">BRIGHT LEDGER</text>
      <text x="0" y="118" font-size="60" textLength="368" lengthAdjust="spacingAndGlyphs">HIDDEN KEYS</text>
    </svg>
    <div class="hero-art" role="img" aria-label="Illustration of a blue credit card with banknotes fanning out above it and a rising zigzag arrow"></div>
    <div class="rule"></div>
    <p class="subtitle">
      <span class="subtitle__light">The Quick Lift and Mend</span>
      <span class="subtitle__bold">Manual for Stellar Borrowing</span>
    </p>
    <p class="author">GIDEON VARLY</p>
    <svg class="corner-card" viewBox="0 0 82 141" role="img" aria-label="Corner illustration of a tilted blue credit card">
      <polygon points="82,0 82,141 55,141 0,80" fill="var(--card-blue)"/>
    </svg>
  </section>

  <section class="cover cover--four">
    <p class="series">VARLY FINANCIAL LITERACY PROGRAM</p>
    <svg class="title" viewBox="0 0 368 124" aria-label="Bright Ledger Hidden Keys">
      <text x="0" y="56" font-size="78" textLength="368" lengthAdjust="spacingAndGlyphs">BRIGHT LEDGER</text>
      <text x="0" y="118" font-size="60" textLength="368" lengthAdjust="spacingAndGlyphs">HIDDEN KEYS</text>
    </svg>
    <div class="hero-art" role="img" aria-label="Illustration of a blue credit card with banknotes fanning out above it and a rising zigzag arrow"></div>
    <div class="rule"></div>
    <p class="subtitle">
      <span class="subtitle__light">The Quick Lift and Mend</span>
      <span class="subtitle__bold">Manual for Stellar Borrowing</span>
    </p>
    <p class="author">GIDEON VARLY</p>
    <svg class="corner-card" viewBox="0 0 82 141" role="img" aria-label="Corner illustration of a tilted blue credit card">
      <polygon points="82,0 82,141 55,141 0,80" fill="var(--card-blue)"/>
    </svg>
  </section>

  <p class="option-label option-label--three">OPTION 03</p>
  <p class="option-label option-label--four">OPTION 04</p>

</main>
</body>
</html>
```